[WEB DESIGN - Start-up] Online LOANS against Luxury Assets - Needs a Web Design

Hello,
We need a web design for a new company. We make online LOANS against Luxury assets.
The name is private, that's why you could remplace it by the term "LOGO" or "ENTERPRISE".

In attachments, you'll find few models that we would like. Nonetheless, we don't want a copy of these screenshots. They are only prototypes that we made. Here we expect you to lead a professional web Design with your intuition and your ideas.

The final design should communicate start-up spirit, professionalism and fluidity.

Best Regards.

Industry/Entity Type

Finance

Number of Pages Required

2 page

Font styles to use
Sans Serif

Colors
f78f20
ffffff
b2b2b2
e9e9e9

Requirements
Must have
• The designer will draw on the 2015 web trends.
• The subject site is serious (loans against luxury assets), but the site should be modern and pleasant.
• PLEASE REFER YOU TO MY MODEL ( ATTACHMENTS)
Nice to have
• Surprise-me ! Welcome to a lot of imagination.

```html
<!DOCTYPE html>
<html lang="fr">
<head>
<meta charset="utf-8">
<title>Lumen Prêt — Prêts contre biens de luxe</title>
<link rel="stylesheet" href="https://fonts.googleapis.com/css2?family=Lato:wght@300;400;700&family=Cinzel:wght@400;700&display=swap">
<style>
:root{
  --orange:#f78f20;
  --white:#ffffff;
  --grey:#b2b2b2;
  --light:#e9e9e9;
  --text:#555555;
  --dark:#2e2e2e;
  --darker:#232323;
  --paper:#f5f5f5;
}
*{box-sizing:border-box;margin:0;padding:0}
html,body{width:1200px;height:3028px;overflow:hidden}
body{font-family:'Lato',sans-serif;color:var(--text);background:var(--white)}
.page{position:relative;width:1200px;height:3028px}

/* header */
.site-header{height:112px;display:flex;align-items:center;justify-content:space-between;padding:0 120px;border-top:6px solid var(--orange)}
.brand{display:flex;align-items:center;gap:14px;font-size:38px;font-weight:700;color:#4a4a4a;letter-spacing:.5px}
.brand-dot{width:40px;height:40px;border-radius:50%;background:var(--orange)}
.main-nav{display:flex;gap:30px;align-items:center}
.main-nav a{font-variant:small-caps;font-size:19px;color:#777;text-decoration:none;letter-spacing:1px}
.main-nav a.is-active{background:var(--orange);color:var(--white);padding:8px 22px;border-radius:20px}

/* hero */
.hero{position:relative;height:428px;background:linear-gradient(100deg,#0d0d0d 0%,#2a2a2a 45%,#3a3530 70%,#141414 100%)}
.hero-visual{position:absolute;inset:0}
.hero-watch{position:absolute;left:150px;top:70px;width:430px;height:300px;border-radius:50%;background:radial-gradient(ellipse at center,#6f5a2c 0%,#3a3124 45%,rgba(20,20,20,0) 72%)}
.hero-hand{position:absolute;right:40px;top:250px;width:400px;height:180px;background:radial-gradient(ellipse at 60% 60%,#b98c6f 0%,#6d4f3c 40%,rgba(30,30,30,0) 72%)}
.hero-title{position:absolute;right:120px;top:50px;text-align:right;font-family:'Cinzel',serif;color:var(--white);font-size:52px;line-height:64px;letter-spacing:1px}
.slider-arrow{position:absolute;top:190px;width:46px;height:46px;border-radius:50%;background:rgba(255,255,255,.2);display:flex;align-items:center;justify-content:center}
.slider-arrow.prev{left:40px}
.slider-arrow.next{right:40px}

/* features */
.features{height:348px;display:flex;justify-content:center;gap:0;padding-top:40px}
.feature{width:248px;text-align:center}
.feature-ring{width:176px;height:176px;margin:0 auto;border-radius:50%;border:14px solid var(--light);display:flex;align-items:center;justify-content:center}
.feature-title{margin-top:18px;font-variant:small-caps;font-size:26px;font-weight:700;color:var(--orange);letter-spacing:1px}
.feature-text{margin:8px auto 0;width:200px;font-size:13px;line-height:18px;color:#999}

/* goods */
.goods{height:1112px;background:var(--light);padding-top:36px}
.section-title{text-align:center;font-variant:small-caps;font-size:38px;font-weight:400;color:var(--orange);letter-spacing:1.5px}
.goods-grid{display:grid;grid-template-columns:repeat(4,232px);column-gap:16px;row-gap:22px;justify-content:center;margin-top:38px}
.good-tile{height:232px}
.good-label{height:56px;line-height:50px;text-align:center;font-variant:small-caps;font-size:20px;color:#555;letter-spacing:1px}

/* help */
.help{height:360px;padding-top:54px}
.help .section-title{font-size:40px}
.help-columns{display:flex;justify-content:center;gap:80px;margin-top:38px}
.help-item{width:270px;text-align:center}
.help-icon{height:140px;display:flex;align-items:flex-end;justify-content:center}
.help-text{margin-top:18px;font-size:16px;line-height:24px;color:#666}
.help-text strong{display:block;font-size:24px;color:var(--orange);font-weight:700}
.help-link{color:var(--orange);font-weight:700;font-size:19px;line-height:26px}

/* testimonials and figures */
.proof{height:400px;background:var(--paper);display:flex;gap:70px;padding:40px 120px 0}
.block-title{font-variant:small-caps;font-size:26px;color:#444;letter-spacing:1px;border-bottom:2px solid var(--light);padding-bottom:8px}
.block-title span{color:var(--orange)}
.testimonials{width:620px}
.testimonial{display:flex;gap:26px;align-items:flex-start;margin-top:26px}
.testimonial.reverse{flex-direction:row-reverse}
.avatar-wrap{width:84px;text-align:center;flex:none}
.avatar{width:76px;height:76px;border-radius:50%;background:radial-gradient(circle at 50% 40%,#b7a08c,#5e5048);margin:0 auto}
.avatar-name{font-size:12px;margin-top:6px;color:#888}
.quote{font-size:14px;line-height:21px;color:#777}
.quote::before{content:"\201C";color:var(--orange);font-size:28px;font-weight:700;margin-right:6px;vertical-align:-8px}
.figures{width:330px}
.counter{display:flex;gap:8px;margin-top:26px}
.digit{width:70px;height:62px;background:#1d1d1d;color:var(--white);font-size:36px;font-weight:700;display:flex;align-items:center;justify-content:center;border-radius:4px;position:relative}
.digit::after{content:"";position:absolute;left:0;right:0;top:50%;height:2px;background:#000}
.figure-text{margin-top:12px;font-size:13px;line-height:19px;color:#888}

/* footer */
.site-footer{height:240px;background:var(--dark);color:#bbb;display:flex;gap:70px;padding:32px 120px 0}
.footer-col h4{font-variant:small-caps;font-weight:400;font-size:18px;color:var(--white);letter-spacing:1px;border-bottom:1px solid #555;padding-bottom:8px;margin-bottom:14px}
.footer-about{width:300px;font-size:13px;line-height:19px}
.footer-links{width:290px;display:flex;gap:40px}
.footer-links ul{list-style:none;font-size:13px;line-height:22px}
.footer-links li::before{content:"› ";color:var(--orange)}
.footer-contact{width:300px;font-size:13px;line-height:19px}
.contact-line{display:flex;gap:10px;align-items:flex-start;margin-bottom:10px}
.copyright{height:28px;background:var(--orange);color:var(--white);font-size:12px;text-align:center;line-height:28px}
</style>
</head>
<body>
<div class="page">

<header class="site-header">
  <div class="brand"><span class="brand-dot"></span>Lumen Prêt</div>
  <nav class="main-nav">
    <a href="#" class="is-active">Concept</a>
    <a href="#">Les Biens</a>
    <a href="#">Estimation</a>
    <a href="#">FAQ</a>
    <a href="#">Nous Contacter</a>
  </nav>
</header>

<section class="hero">
  <div class="hero-visual" role="img" aria-label="Photo d'une montre de luxe et d'un bracelet en or, à droite une main tenant des billets">
    <div class="hero-watch"></div>
    <div class="hero-hand"></div>
  </div>
  <h1 class="hero-title">On se lasse de tout,<br>sauf de l'argent.</h1>
  <span class="slider-arrow prev"><svg width="18" height="18" viewBox="0 0 18 18"><path d="M12 2 L5 9 L12 16" fill="none" stroke="#fff" stroke-width="2.5"/></svg></span>
  <span class="slider-arrow next"><svg width="18" height="18" viewBox="0 0 18 18"><path d="M6 2 L13 9 L6 16" fill="none" stroke="#fff" stroke-width="2.5"/></svg></span>
</section>

<section class="features">
  <div class="feature">
    <div class="feature-ring">
      <svg width="70" height="70" viewBox="0 0 70 70"><circle cx="35" cy="35" r="26" fill="none" stroke="var(--orange)" stroke-width="5"/><path d="M35 20 V35 L45 42" fill="none" stroke="var(--orange)" stroke-width="5" stroke-linecap="round"/></svg>
    </div>
    <div class="feature-title">Estimation</div>
    <p class="feature-text">Envoyez les photos de votre bien et recevez une première estimation sous 24 heures.</p>
  </div>
  <div class="feature">
    <div class="feature-ring">
      <svg width="76" height="60" viewBox="0 0 76 60"><rect x="4" y="8" width="62" height="42" rx="5" fill="var(--orange)"/><rect x="4" y="17" width="62" height="8" fill="#fff"/><rect x="12" y="34" width="20" height="6" fill="#fff"/></svg>
    </div>
    <div class="feature-title">Paiement</div>
    <p class="feature-text">Le montant du prêt est versé rapidement sur votre compte, sans démarche complexe.</p>
  </div>
  <div class="feature">
    <div class="feature-ring">
      <svg width="60" height="72" viewBox="0 0 60 72"><path d="M15 32 V20 a15 15 0 0 1 30 0 V32" fill="none" stroke="var(--orange)" stroke-width="6"/><rect x="6" y="30" width="48" height="38" rx="5" fill="var(--orange)"/><circle cx="30" cy="47" r="5" fill="#fff"/><rect x="28" y="48" width="4" height="11" fill="#fff"/></svg>
    </div>
    <div class="feature-title">Sécurisation</div>
    <p class="feature-text">Votre objet est assuré et conservé dans un coffre sécurisé pendant toute la durée.</p>
  </div>
  <div class="feature">
    <div class="feature-ring">
      <svg width="64" height="70" viewBox="0 0 64 70"><path d="M20 22 V16 a12 12 0 0 1 24 0 V22" fill="none" stroke="var(--orange)" stroke-width="5"/><path d="M8 22 H56 L52 66 H12 Z" fill="var(--orange)"/></svg>
    </div>
    <div class="feature-title">Rachat</div>
    <p class="feature-text">Remboursez votre prêt à votre rythme et récupérez votre bien en toute sérénité.</p>
  </div>
</section>

<section class="goods">
  <h2 class="section-title">Les Biens Que Nous Acceptons</h2>
  <div class="goods-grid">
    <div><div class="good-tile" role="img" aria-label="Photo d'un piano et d'instruments de musique" style="background:linear-gradient(160deg,#6e5a48,#2b2420)"></div><div class="good-label">Instrument</div></div>
    <div><div class="good-tile" role="img" aria-label="Photo d'un tableau ancien dans une galerie" style="background:linear-gradient(160deg,#8a6f45,#3c3226)"></div><div class="good-label">Art : Tableaux</div></div>
    <div><div class="good-tile" role="img" aria-label="Photo de pierres précieuses colorées" style="background:linear-gradient(135deg,#3c6fa0,#b0487a 50%,#d6b24a)"></div><div class="good-label">Pierres Précieuses</div></div>
    <div><div class="good-tile" role="img" aria-label="Photo de bouteilles de vin et de cognac" style="background:linear-gradient(160deg,#c9864a,#5a2a14)"></div><div class="good-label">Vins &amp; Spiritueux</div></div>

    <div><div class="good-tile" role="img" aria-label="Photo d'une sculpture moderne" style="background:linear-gradient(160deg,#d8d4cf,#7c756d)"></div><div class="good-label">Art : Sculptures</div></div>
    <div><div class="good-tile" role="img" aria-label="Photo d'une pile de mobilier en papier coloré" style="background:linear-gradient(160deg,#e3ddd5,#a99f95)"></div><div class="good-label">Mat Propre</div></div>
    <div><div class="good-tile" role="img" aria-label="Photo de bijoux en or" style="background:linear-gradient(160deg,#e3c36a,#8a6420)"></div><div class="good-label">Bijoux</div></div>
    <div><div class="good-tile" role="img" aria-label="Photo d'une montre de luxe" style="background:linear-gradient(160deg,#9c8f80,#2f2b28)"></div><div class="good-label">Montres</div></div>

    <div><div class="good-tile" role="img" aria-label="Photo d'une voiture ancienne" style="background:linear-gradient(160deg,#9a9a96,#3a3a38)"></div><div class="good-label">Véhicules</div></div>
    <div><div class="good-tile" role="img" aria-label="Photo de lingots d'or" style="background:linear-gradient(160deg,#e8b84a,#7a4e12)"></div><div class="good-label">Métaux Précieux</div></div>
    <div><div class="good-tile" role="img" aria-label="Photo d'un sac de maroquinerie de luxe" style="background:linear-gradient(160deg,#7a5a34,#2e2216)"></div><div class="good-label">Maroquinerie</div></div>
    <div><div class="good-tile" role="img" aria-label="Photo d'un téléphone rétro sur fond clair" style="background:linear-gradient(160deg,#f3f1ee,#b7b0a6)"></div><div class="good-label">High-Tech</div></div>
  </div>
</section>

<section class="help">
  <h2 class="section-title">Besoin d'aide ? Nous sommes à votre écoute</h2>
  <div class="help-columns">
    <div class="help-item">
      <div class="help-icon">
        <svg width="140" height="110" viewBox="0 0 140 110"><path d="M10 40 Q10 10 70 10 Q130 10 130 40 L130 48 L100 48 L100 34 L40 34 L40 48 L10 48 Z" fill="var(--orange)"/><path d="M30 56 H110 L122 104 H18 Z" fill="var(--orange)"/><circle cx="70" cy="78" r="14" fill="#fff"/></svg>
      </div>
      <p class="help-text">Du lundi au Vendredi de 9h à 19h<strong>01 42 55 18 60</strong></p>
    </div>
    <div class="help-item">
      <div class="help-icon">
        <svg width="120" height="130" viewBox="0 0 120 130"><circle cx="60" cy="38" r="30" fill="var(--orange)"/><text x="60" y="51" font-family="Lato,sans-serif" font-weight="700" font-size="38" fill="#fff" text-anchor="middle">?</text><path d="M20 128 Q20 80 60 80 Q100 80 100 128 Z" fill="var(--orange)"/></svg>
      </div>
      <p class="help-text"><span class="help-link">Questions<br>Fréquentes</span></p>
    </div>
    <div class="help-item">
      <div class="help-icon">
        <svg width="140" height="110" viewBox="0 0 140 110"><rect x="12" y="24" width="116" height="80" rx="4" fill="none" stroke="var(--orange)" stroke-width="5"/><path d="M14 26 L70 70 L126 26" fill="none" stroke="var(--orange)" stroke-width="5"/><path d="M40 6 L50 16 M70 0 V14 M100 6 L90 16" stroke="var(--orange)" stroke-width="4" stroke-linecap="round"/></svg>
      </div>
      <p class="help-text"><span class="help-link">Formulaire de contact</span><br>Ou<br><span class="help-link">contact@lumenpret.fr</span></p>
    </div>
  </div>
</section>

<section class="proof">
  <div class="testimonials">
    <h3 class="block-title"><span>Derniers</span> Témoignages</h3>
    <div class="testimonial">
      <div class="avatar-wrap"><div class="avatar" role="img" aria-label="Portrait d'un client"></div><div class="avatar-name">Marc D.</div></div>
      <p class="quote">Service rapide et très professionnel. J'ai obtenu mon prêt en deux jours en laissant ma montre en garantie, puis je l'ai récupérée sans aucune difficulté. L'équipe a su répondre à toutes mes questions avec clarté.</p>
    </div>
    <div class="testimonial reverse">
      <div class="avatar-wrap"><div class="avatar" role="img" aria-label="Portrait d'une cliente"></div><div class="avatar-name">Sophie L.</div></div>
      <p class="quote">Une solution idéale pour financer un projet sans vendre mes bijoux de famille. L'estimation était juste, le suivi transparent et la restitution s'est faite dans les délais annoncés.</p>
    </div>
  </div>
  <div class="figures">
    <h3 class="block-title"><span>Quelques</span> Chiffres</h3>
    <div class="counter"><span class="digit">01</span><span class="digit">08</span><span class="digit">43</span><span class="digit">42</span></div>
    <p class="figure-text">Euros prêtés à nos clients depuis le lancement de notre service en ligne.</p>
    <div class="counter"><span class="digit">01</span><span class="digit">08</span><span class="digit">43</span><span class="digit">42</span></div>
    <p class="figure-text">Biens de luxe estimés et conservés en toute sécurité par nos experts.</p>
  </div>
</section>

<footer class="site-footer">
  <div class="footer-col footer-about">
    <h4>Vendre ou voir se racheter</h4>
    <p>Lumen Prêt vous permet d'obtenir rapidement des liquidités en confiant un bien de valeur. Nous estimons, assurons et conservons votre objet jusqu'au remboursement complet du prêt, en toute confidentialité.</p>
  </div>
  <div class="footer-col">
    <h4>Liens rapides</h4>
    <div class="footer-links">
      <ul><li>Accueil</li><li>Concept</li><li>Les Biens</li><li>Estimation</li><li>FAQ</li><li>Nous contacter</li></ul>
      <ul><li>Mes crédits</li><li>Vendre un bien</li><li>Nos garanties</li></ul>
    </div>
  </div>
  <div class="footer-col footer-contact">
    <h4>Contactez-nous</h4>
    <div class="contact-line"><svg width="14" height="18" viewBox="0 0 14 18"><path d="M7 0 A7 7 0 0 1 14 7 C14 12 7 18 7 18 C7 18 0 12 0 7 A7 7 0 0 1 7 0 Z" fill="var(--orange)"/><circle cx="7" cy="7" r="2.5" fill="#2e2e2e"/></svg><span>Lumen Prêt<br>12 rue des Orfèvres<br>75002 Paris, France</span></div>
    <p>Service client disponible du lundi au vendredi. Téléphone : 01 42 55 18 60<br>contact@lumenpret.fr</p>
  </div>
</footer>
<div class="copyright">© 2015 Lumen Prêt — Tous droits réservés</div>

</div>
</body>
</html>
```